Design a Book Cover for a Bill Tracker Logbook

We are looking for a designer to create a book cover for a bill tracker. The detailed instructions and interior pages are attached. For those who are new to RVM, the cover template is also attached.
Please be creative and focus on creating a trustworthy, reliable, modern, and secure feeling based on the theme. You are allowed to use downloaded templates, but you must provide commercial licenses.
Attention: We are happy to pay extra tip if you are selected with a really high quality design.
US

```html
<!DOCTYPE html>
<html lang="en">
<head>
<meta charset="utf-8">
<title>Bill Tracker &amp; Password Log – Book Cover</title>
<link href="https://fonts.googleapis.com/css2?family=Montserrat:wght@600&family=Playfair+Display:wght@500&display=swap" rel="stylesheet">
<style>
  :root {
    --cover-blue: #0063cc;
    --page-blue: #0062cc;
    --title-yellow: #ffeb5c;
    --label-navy: #0d3b8c;
    --label-text: #f4f6ff;
    --art-light: #cfe2fb;
    --art-mid: #4d95ee;
    --art-deep: #0b4aa8;
  }
  * { margin: 0; padding: 0; box-sizing: border-box; }
  html, body { width: 1200px; height: 1200px; overflow: hidden; }
  body { background: var(--page-blue); position: relative; }

  .cover {
    position: absolute; left: 35px; top: 237px;
    width: 1137px; height: 731px;
    background: var(--cover-blue);
  }

  .title {
    position: absolute; text-align: center;
    font-family: "Playfair Display", Georgia, serif; font-weight: 500;
    color: var(--title-yellow); line-height: 1; letter-spacing: -0.02em;
    white-space: nowrap;
  }
  .amp-row { position: absolute; display: flex; align-items: center; justify-content: space-between; }
  .amp-row .rule { height: 2px; background: var(--title-yellow); }
  .amp-row .amp {
    font-family: "Playfair Display", Georgia, serif; font-weight: 500;
    color: var(--title-yellow); line-height: 1;
  }

  /* back cover */
  .back-title-1 { left: 0; width: 568px; top: 38px; font-size: 54px; }
  .back-amp { left: 117px; width: 334px; top: 108px; }
  .back-amp .rule { width: 103px; }
  .back-amp .amp { font-size: 56px; }
  .back-title-2 { left: 0; width: 568px; top: 170px; font-size: 54px; }
  .back-message {
    position: absolute; left: 38px; top: 248px; width: 493px;
    font-family: "Montserrat", Arial, sans-serif; font-weight: 600;
    font-size: 25px; line-height: 33px; color: var(--title-yellow);
    text-align: justify; text-align-last: center; letter-spacing: 0.01em;
  }
  .publisher {
    position: absolute; left: 0; width: 568px; top: 570px;
    display: flex; align-items: center; justify-content: center; gap: 10px;
    font-family: "Montserrat", Arial, sans-serif; font-weight: 600;
    font-size: 18px; color: var(--title-yellow); letter-spacing: 0.04em;
  }
  .publisher .dot { width: 14px; height: 14px; border-radius: 50%; background: var(--title-yellow); }

  /* spine */
  .spine-text {
    position: absolute; left: 564px; top: 291px; width: 10px; height: 170px;
    writing-mode: vertical-rl;
    font-family: "Playfair Display", Georgia, serif; font-size: 7px;
    letter-spacing: 0.12em; color: var(--label-text); white-space: nowrap;
  }

  /* front cover */
  .front-title-1 { left: 620px; width: 484px; top: 36px; font-size: 70px; }
  .front-amp { left: 639px; width: 429px; top: 120px; }
  .front-amp .rule { width: 132px; }
  .front-amp .amp { font-size: 74px; }
  .front-title-2 { left: 600px; width: 524px; top: 204px; font-size: 70px; }

  .features {
    position: absolute; left: 614px; top: 291px; width: 480px; height: 58px;
    font-family: "Playfair Display", Georgia, serif; font-size: 15.5px;
    color: var(--label-text);
  }
  .feature {
    position: absolute; background: var(--label-navy);
    padding: 0 3px; line-height: 18px; white-space: nowrap;
  }
  .feature.passwords { left: 0; top: 3px; }
  .feature.years { left: 1px; top: 41px; }
  .feature.payments { left: 258px; top: 3px; }
  .feature.pages { left: 258px; top: 41px; width: 100px; }
  .features .divider {
    position: absolute; left: 245px; top: 0; width: 2px; height: 56px;
    background: var(--label-navy);
  }

  .bills-art {
    position: absolute; left: 665px; top: 366px; width: 375px; height: 341px;
    border-radius: 20px 20px 50% 50% / 20px 20px 14% 14%;
    background: linear-gradient(160deg, var(--art-light) 0%, var(--art-mid) 55%, var(--art-deep) 100%);
  }
</style>
</head>
<body>
  <main class="cover">
    <section class="back-cover">
      <h2 class="title back-title-1">BILL TRACKER</h2>
      <div class="amp-row back-amp"><span class="rule"></span><span class="amp">&amp;</span><span class="rule"></span></div>
      <h2 class="title back-title-2">PASSWORD LOG</h2>
      <p class="back-message">Thank you for choosing “Bill Tracker &amp; Password Log”, please leave a review on Bookvale if you find it helpful in your life, this will help us produce more high-quality content. Thank you.</p>
      <div class="publisher"><span class="dot"></span><span>LENA VARROW</span></div>
    </section>

    <div class="spine-text">BILL TRACKER &amp; PASSWORD LOG</div>

    <section class="front-cover">
      <h1 class="title front-title-1">BILL TRACKER</h1>
      <div class="amp-row front-amp"><span class="rule"></span><span class="amp">&amp;</span><span class="rule"></span></div>
      <h1 class="title front-title-2">PASSWORD LOG</h1>
      <div class="features">
        <span class="feature passwords">Save Passwords and Contacts</span>
        <span class="feature years">FROM 20__ TO 20__</span>
        <span class="divider"></span>
        <span class="feature payments">Track Payments up to 8 Years</span>
        <span class="feature pages">100+ Pages</span>
      </div>
      <div class="bills-art" role="img" aria-label="Illustration of a pile of bills, invoices and envelopes marked past due, final notice and overdue"></div>
    </section>
  </main>
</body>
</html>
```